Website design for KOVIL – data platform for healthcare & social housing

We’re looking for a clean, modern multi-page website design for KOVIL — a data platform for healthcare and social housing.

📎 Please read the attached PDF for full structure, context, and design guidance.
The briefing is essential to understanding this project.

➡️ For the initial submission, only the homepage design (including header and footer) is required.

This will help us assess design direction and fit.

The full project includes four levels (homepage, general page, product overview, and product detail), which will be completed after selecting the final designer.

Industry/Entity Type

data platform for healthcare & social housing

Number of Pages Required

1 page

Font styles to use
Sans Serif

Requirements
Must have
• Please read the attached PDF
Nice to have
Should not have

```html
<!DOCTYPE html>
<html lang="en">
<head>
<meta charset="utf-8">
<title>KOVIL – Data for Healthcare and Social Housing</title>
<link rel="stylesheet" href="https://fonts.googleapis.com/css2?family=Newsreader:opsz,wght@6..72,400;6..72,500&family=Red+Hat+Display:wght@400;500;700;900&display=swap">
<style>
  :root{
    --navy:#1a4a86;
    --ink:#1f4784;
    --hero-bg:#eceee9;
    --page-bg:#f4f4f1;
    --rule:#dcdcd6;
    --white:#ffffff;
    --orange:#e48a2a;
  }
  *{box-sizing:border-box;margin:0;padding:0}
  html,body{width:1200px;height:3876px;overflow:hidden}
  body{position:relative;background:var(--page-bg);font-family:"Red Hat Display",sans-serif;color:var(--ink)}
  .abs{position:absolute}
  .serif{font-family:"Newsreader",serif;font-weight:400}
  .header{left:0;top:0;width:1200px;height:84px;background:var(--white)}
  .brand{left:48px;top:20px;font-size:30px;font-weight:700;letter-spacing:4px;color:var(--navy)}
  .nav-home{left:942px;top:31px;font-size:12px;font-weight:500;color:#222;padding-bottom:4px;border-bottom:1px solid #222}
  .btn-outline{left:1003px;top:15px;width:158px;height:46px;border:1.5px solid var(--navy);font-size:12px;font-weight:500;color:var(--navy);display:flex;align-items:center;justify-content:center;letter-spacing:.3px}
  .hero{left:0;top:84px;width:1200px;height:740px;background:var(--hero-bg)}
  .hero-title{left:60px;top:126px;font-size:73px;line-height:90px;color:var(--navy);letter-spacing:-1.2px}
  .hero-sub{left:61px;top:325px;font-size:15px}
  .photo{background:linear-gradient(135deg,#cfd9e4,#eef0f0 55%,#b9c4d0)}
  .eyebrow{font-size:15px}
  .h2{font-size:30px;line-height:36px;color:var(--navy)}
  .body{font-size:15px;line-height:22.5px}
  .btn{background:var(--navy);color:var(--white);font-size:12px;font-weight:700;display:flex;align-items:center;justify-content:center}
  .rule{height:1px;background:var(--rule);width:428px;left:635px}
  .stat{font-size:50px;font-weight:900;color:var(--navy)}
  .member-photo{background:linear-gradient(180deg,#9a9a9a,#3e3e3e)}
  .member-name{font-size:23px;color:var(--navy)}
  .member-role{font-size:17px}
  .cta{left:0;top:2888px;width:1200px;height:553px;background:linear-gradient(135deg,#6d6f73,#3a3b3e 45%,#2a2b2e 70%,#5d5a55)}
  .cta-shade{left:0;top:2888px;width:1200px;height:553px;background:rgba(20,24,32,.35)}
  .cta-btn{top:3313px;width:208px;height:53px;background:var(--navy);color:var(--white);font-size:12px;font-weight:500;display:flex;align-items:center;justify-content:center}
  .footer{left:0;top:3441px;width:1200px;height:435px;background:var(--navy);color:var(--white)}
  .f-text{color:var(--white)}
</style>
</head>
<body>
  <header class="abs header" aria-label="Site header"></header>
  <div class="abs brand">KOVIL</div>
  <div class="abs nav-home">HOME</div>
  <div class="abs btn-outline">GET STARTED</div>

  <section class="abs hero"></section>
  <h1 class="abs hero-title serif">KOVIL: Transforming Data for<br>Healthcare and Social Housing</h1>
  <p class="abs hero-sub">Empowering Better Decisions Through Data Insights</p>
  <div class="abs photo" style="left:62px;top:364px;width:1076px;height:405px" role="img" aria-label="Person writing in a notebook beside a laptop"></div>

  <div class="abs" style="left:48px;top:856px;width:518px;height:398px;background:linear-gradient(135deg,#c9b160,#1b1e22 25%,#101318 70%,#b59a48)" role="img" aria-label="Tablet screen showing financial charts"></div>
  <p class="abs eyebrow" style="left:647px;top:870px">Transform Your Data into Insights</p>
  <h2 class="abs h2 serif" style="left:647px;top:905px;width:500px">Unlock the Power of Data with KOVIL's User-Friendly Platform</h2>
  <p class="abs body" style="left:647px;top:1004px;width:440px">KOVIL offers powerful data analytics and reporting tools tailored for healthcare and social housing sectors, ensuring informed decision-making and improved outcomes.</p>
  <div class="abs btn" style="left:647px;top:1120px;width:233px;height:46px">Get Started</div>

  <p class="abs eyebrow" style="left:63px;top:1335px">Comprehensive Reporting at Your Fingertips</p>
  <h2 class="abs h2 serif" style="left:63px;top:1369px;width:520px">Experience Seamless Data Analytics and Reporting with KOVIL</h2>
  <p class="abs body" style="left:63px;top:1468px;width:440px">Our intuitive interface simplifies data management, making it accessible for all users, regardless of technical expertise.</p>
  <div class="abs btn" style="left:63px;top:1561px;width:233px;height:46px">Learn More</div>
  <div class="abs" style="left:635px;top:1320px;width:519px;height:389px;background:linear-gradient(180deg,#dfe3e6,#b9b9b3 55%,#7a5a40)" role="img" aria-label="Two people talking in chairs by a bright window"></div>

  <h2 class="abs serif" style="left:138px;top:1845px;font-size:56px;line-height:64px;color:var(--navy)">Data Management<br>Excellence</h2>
  <p class="abs body" style="left:138px;top:2000px;width:410px">KOVIL empowers healthcare and social housing organizations with unparalleled data management capabilities, ensuring informed decision-making and improved outcomes.</p>
  <div class="abs rule" style="top:1772px"></div>
  <div class="abs stat" style="left:633px;top:1808px">95%</div>
  <p class="abs body" style="left:635px;top:1880px;width:430px">of users report enhanced data accuracy and reliability after implementing KOVIL's platform.</p>
  <div class="abs rule" style="top:1960px"></div>
  <div class="abs stat" style="left:633px;top:1996px">80%</div>
  <p class="abs body" style="left:635px;top:2068px;width:430px">of clients experience a significant reduction in data processing time, allowing for quicker insights and actions.</p>
  <div class="abs rule" style="top:2170px"></div>

  <h2 class="abs serif" style="left:72px;top:2246px;font-size:28px;color:var(--navy)">Meet Our Team</h2>
  <p class="abs body" style="left:72px;top:2298px;width:830px">Our dedicated team of experts is committed to advancing healthcare and social housing through innovative data solutions. Each member brings a wealth of experience and specialized knowledge to support KOVIL's mission.</p>

  <div class="abs member-photo" style="left:78px;top:2435px;width:248px;height:316px" role="img" aria-label="Team member portrait, black and white"></div>
  <div class="abs member-photo" style="left:344px;top:2435px;width:249px;height:316px" role="img" aria-label="Team member portrait, black and white"></div>
  <div class="abs member-photo" style="left:609px;top:2435px;width:248px;height:316px" role="img" aria-label="Team member portrait, black and white"></div>
  <div class="abs member-photo" style="left:874px;top:2435px;width:248px;height:316px" role="img" aria-label="Team member portrait, black and white"></div>
  <div class="abs member-name serif" style="left:92px;top:2762px">Dr. Nora Valdane</div>
  <div class="abs member-role" style="left:92px;top:2794px">Chief Data Scientist</div>
  <div class="abs member-name serif" style="left:357px;top:2762px">Tobias Wrenfield</div>
  <div class="abs member-role" style="left:357px;top:2794px">Product Manager</div>
  <div class="abs member-name serif" style="left:622px;top:2762px">Lena Marquette</div>
  <div class="abs member-role" style="left:622px;top:2794px">Lead Software Engineer</div>
  <div class="abs member-name serif" style="left:888px;top:2762px">Aaron Delcourt</div>
  <div class="abs member-role" style="left:888px;top:2794px">Data Analyst</div>

  <div class="abs cta" role="img" aria-label="Laptop showing charts next to a tablet with a calendar"></div>
  <div class="abs cta-shade"></div>
  <p class="abs" style="left:0;top:2962px;width:1200px;text-align:center;font-size:12px;color:var(--white)">TRANSFORMING DATA INTO INSIGHTS</p>
  <h2 class="abs serif" style="left:0;top:3036px;width:1200px;text-align:center;font-size:44px;color:var(--white)">Get Started with KOVIL</h2>
  <p class="abs" style="left:455px;top:3133px;width:290px;text-align:center;font-size:14px;line-height:18.5px;color:var(--white)">Unlock the potential of your data with KOVIL. Sign up for a demo today to see how our platform can enhance your healthcare and social housing initiatives. Our team is ready to assist you in making informed decisions backed by powerful analytics.</p>
  <div class="abs cta-btn" style="left:254px">Request a Demo</div>
  <div class="abs cta-btn" style="left:496px">Contact Us</div>
  <div class="abs cta-btn" style="left:738px">Learn More</div>

  <footer class="abs footer"></footer>
  <div class="abs f-text" style="left:38px;top:3508px;font-size:24px;font-weight:900">KOVIL</div>
  <div class="abs f-text" style="left:614px;top:3514px;font-size:14px;font-weight:500;padding-bottom:5px;border-bottom:1px solid #fff">Home</div>
  <p class="abs f-text serif" style="left:38px;top:3620px;font-size:23px;line-height:30px">This is the text area for this<br>paragraph.</p>
  <div class="abs f-text" style="left:123px;top:3695px;font-size:12px;text-decoration:underline">Learn more</div>
  <div class="abs f-text serif" style="left:614px;top:3628px;font-size:19px">Contact</div>
  <div class="abs f-text" style="left:614px;top:3670px;font-size:16px;line-height:24px">hello@kovilmail.net<br>+000 1234 5678</div>
  <div class="abs f-text serif" style="left:902px;top:3628px;font-size:19px">Address</div>
  <div class="abs f-text" style="left:902px;top:3670px;font-size:16px;line-height:24px">Harbor Lane, Eastvale,<br>Northland</div>
  <div class="abs" style="left:38px;top:3805px;width:1124px;height:1px;background:rgba(255,255,255,.5)"></div>
  <div class="abs f-text" style="left:38px;top:3843px;font-size:12px">© 2025 All Rights Reserved | Company Name</div>
  <svg class="abs" style="left:1074px;top:3840px" width="90" height="20" aria-label="Social links">
    <circle cx="8" cy="10" r="7" fill="#fff"/>
    <circle cx="41" cy="10" r="7" fill="#fff"/>
    <circle cx="74" cy="10" r="7" fill="#fff"/>
  </svg>
</body>
</html>
```